Product Page Images & A+ Content Design for TCG Storage Products

Create a new, cohesive set of Brindle product images (all secondary gallery images) and A+ content modules for Ember Keep Protective Card Sleeves. The goal is to clearly communicate protection, fit, clarity, and archival safety while looking more premium and distinctive than competing sleeve brands.

Primary benefits to communicate:
- Shield your cards from wear – blocks dust and resists surface scratches.
- The perfect fit for your collection – designed to fit all standard trading cards.
- Ultra‑clear smooth finish.
- Archival‑safe high‑quality materials – acid‑free, no PVC, non‑toxic, long‑term storage.

Tone: Premium but approachable, aimed at TCG players and collectors (Tavrinox, KQD, Ra‑Ko‑Zu!, sports cards, etc.). Colour/theme be in keeping with the packaging design. Dark, with a pop of orange. Perhaps subtle textures or patterns, with a mythic/fantasy feel.

Existing product content is attached for reference.

Target Market(s)

Trading card game players and collectors (Tavrinox‑style TCGs, KQD‑style games, Ra‑Ko‑Zu!‑style games, sports cards). Age: Mainly 14–40, skewed to hobbyist young adults. They care about condition and long‑term value of their cards, enjoy customising and protecting decks, responsive to “premium but good value” messaging.

Industry/Entity Type

Trading card accessories / tabletop gaming accessories. Protective sleeves and storage for trading card games and sports cards.

Font styles to use
Sans Serif

Requirements
Must have
• Clear communication of the four key benefits listed in the Project Description. Consistent use of Ember Keep logo and brand colours. Text that is readable on mobile thumbnails. Clean, uncluttered layouts that look professional next to leading competitors.
Nice to have
• Subtle fantasy / “mythic” visual touches that support the brand name (background textures, icons, gentle glow effects). Simple line‑art icons for key benefits (dust, scratch, fit, clarity, archival safe). Visual references to different card types (TCG, sports, etc.) using generic, non‑IP artwork. Light environmental storytelling (desk, playmat, storage box, binder). Lifestyle shots showing people playing or organising their collections.
Should not have
• Any copyrighted or licensed character artwork or logos. Over‑busy backgrounds or textures that distract from the product. Very long text blocks or small copy that is hard to read on mobile. Edgy, aggressive, or dark imagery that clashes with a family‑friendly hobby product. Inconsistent typography or colour schemes across images.

```html
<!DOCTYPE html>
<html lang="en">
<head>
<meta charset="utf-8">
<title>Ember Keep Protective Card Sleeves – Gallery &amp; A+ Modules</title>
<link href="https://fonts.googleapis.com/css2?family=Bebas+Neue&display=swap" rel="stylesheet">
<style>
  :root {
    --page: #ffffff;
    --ink-black: #050403;
    --night: #120b07;
    --ember-deep: #3a1406;
    --ember: #e2531c;
    --flame: #f08a22;
    --gold: #e3c170;
    --gold-deep: #c99a45;
    --white: #ffffff;
    --slate: #1e272c;
    --slate-light: #3a464c;
    --pack-dark: #17120d;
  }
  * { box-sizing: border-box; margin: 0; padding: 0; }
  html, body { width: 1200px; height: 3276px; overflow: hidden; }
  body { background: var(--page); position: relative; font-family: "Bebas Neue", "Arial Narrow", sans-serif; }

  .module { position: absolute; overflow: hidden; }
  .backdrop { position: absolute; inset: 0; }
  .fire-scene { background:
      radial-gradient(ellipse at 80% 95%, rgba(240,138,34,.55), transparent 55%),
      radial-gradient(ellipse at 10% 100%, rgba(226,83,28,.45), transparent 50%),
      linear-gradient(180deg, #1a0d07 0%, #2a1208 60%, #4a1a07 100%); }
  .fire-scene-top { background:
      radial-gradient(ellipse at 50% 0%, rgba(240,138,34,.5), transparent 55%),
      radial-gradient(ellipse at 0% 100%, rgba(226,83,28,.4), transparent 50%),
      linear-gradient(180deg, #2b1207 0%, #160b06 55%, #0c0705 100%); }
  .castle-scene { background:
      radial-gradient(ellipse at 70% 30%, rgba(120,135,140,.35), transparent 60%),
      linear-gradient(180deg, #2c363b 0%, #1b2328 60%, #12181b 100%); }
  .forest-fire-scene { background:
      radial-gradient(ellipse at 60% 90%, rgba(240,110,30,.5), transparent 55%),
      radial-gradient(ellipse at 60% 20%, rgba(200,90,30,.35), transparent 60%),
      linear-gradient(180deg, #3a1a0c 0%, #24100a 55%, #1a0905 100%); }

  .pack { position: absolute;
    background: linear-gradient(180deg, #2a2119 0%, var(--pack-dark) 70%, var(--ember) 100%);
    border: 5px solid #e9e4dc; box-shadow: 0 8px 24px rgba(0,0,0,.55); }

  .headline { position: absolute; color: var(--gold); line-height: 1; letter-spacing: .5px; }
  .subline { position: absolute; color: var(--white); line-height: 1.15; }
  .feature { position: absolute; display: flex; align-items: center; gap: 14px; color: var(--white); line-height: 1.15; }
  .feature svg { flex: none; stroke: var(--white); fill: none; stroke-width: 2.2; stroke-linecap: round; stroke-linejoin: round; }
  .centered { text-align: center; left: 0; right: 0; }

  .ribbon { position: absolute; top: 0; background: var(--ember);
    clip-path: polygon(0 0, 100% 0, 100% 100%, 50% 86%, 0 100%); display: flex; justify-content: center; }
  .ribbon svg { stroke: var(--white); fill: none; stroke-width: 3; stroke-linecap: round; stroke-linejoin: round; }

  .brand-name { position: absolute; color: var(--gold); line-height: .95; }
  .brand-ring { position: absolute; border: 3px solid var(--gold-deep); border-radius: 50%; }

  /* row modules */
  .sq-shield  { left: 0;   top: 0;   width: 572px; height: 572px; }
  .sq-fit     { left: 629px; top: 0; width: 571px; height: 572px; }
  .sq-clear   { left: 0;   top: 619px; width: 572px; height: 572px; }
  .sq-archive { left: 629px; top: 619px; width: 571px; height: 572px; }
  .bn-brand   { left: 0; top: 1247px; width: 1200px; height: 358px; background: var(--ink-black); }
  .bn-shield  { left: 0; top: 1664px; width: 1200px; height: 358px; }
  .bn-fit     { left: 0; top: 2081px; width: 1200px; height: 358px; }
  .bn-clear   { left: 0; top: 2498px; width: 1200px; height: 358px; background: #101315; }
  .bn-archive { left: 0; top: 2915px; width: 1200px; height: 361px; }
</style>
</head>
<body>

<!-- Square 1: Shield -->
<section class="module sq-shield">
  <div class="backdrop fire-scene" role="img" aria-label="Dark background with glowing embers and flames"></div>
  <h2 class="headline" style="left:28px; top:96px; font-size:64px;">Shield your<br>cards from<br>wear</h2>
  <div class="feature" style="left:26px; top:296px; font-size:34px;">
    <svg width="62" height="56" viewBox="0 0 62 56"><path d="M6 10 L26 28 L6 46"/><path d="M18 6 L38 28 L18 50"/><path d="M40 28 H58 M52 22 L58 28 L52 34"/><circle cx="8" cy="28" r="1.5"/><circle cx="14" cy="20" r="1.5"/></svg>
    <span>Blocks dust</span>
  </div>
  <div class="feature" style="left:26px; top:368px; font-size:34px;">
    <svg width="62" height="72" viewBox="0 0 62 72"><rect x="6" y="6" width="24" height="60" rx="3"/><path d="M36 14 L56 6 M34 36 L58 24 M36 58 L56 48"/></svg>
    <span>Resists surface<br>scratches.</span>
  </div>
  <div class="pack" style="left:338px; top:92px; width:250px; height:348px; transform:rotate(-3deg);" role="img" aria-label="Ember Keep protective card sleeves pack, 100 sleeves"></div>
</section>

<!-- Square 2: Fit -->
<section class="module sq-fit">
  <div class="backdrop fire-scene-top" role="img" aria-label="Dark background with a warm flame glow at the top"></div>
  <h2 class="headline centered" style="top:40px; font-size:60px;">The perfect fit for<br>your collection</h2>
  <p class="subline centered" style="top:166px; font-size:37px;">Designed to fit all standard<br>trading cards.</p>
  <div class="pack" style="left:25px; top:305px; width:150px; height:290px;" role="img" aria-label="Ember Keep sleeves pack"></div>
  <div class="pack" style="left:159px; top:271px; width:220px; height:320px;" role="img" aria-label="Ember Keep sleeves pack"></div>
  <div class="pack" style="left:356px; top:343px; width:190px; height:250px;" role="img" aria-label="Ember Keep sleeves pack"></div>
</section>

<!-- Square 3: Clear -->
<section class="module sq-clear">
  <div class="backdrop castle-scene" role="img" aria-label="Misty grey-blue fantasy castle backdrop"></div>
  <div class="pack" style="left:-20px; top:25px; width:272px; height:522px;" role="img" aria-label="Ember Keep protective card sleeves pack, 100 sleeves"></div>
  <h2 class="headline" style="left:277px; top:116px; font-size:58px;">Ultra-clear<br>smooth finish</h2>
  <div class="feature" style="left:277px; top:252px; font-size:25px; align-items:flex-start; gap:14px;">
    <svg width="46" height="46" viewBox="0 0 46 46"><path d="M16 6 L19 17 L30 20 L19 23 L16 34 L13 23 L2 20 L13 17 Z"/><path d="M36 4 L37.5 9 L42 10.5 L37.5 12 L36 17 L34.5 12 L30 10.5 L34.5 9 Z"/><path d="M34 30 L35.5 35 L40 36.5 L35.5 38 L34 43 L32.5 38 L28 36.5 L32.5 35 Z"/></svg>
    <span>Enjoy crystal-clear<br>visibility for vibrant<br>artwork and sharp<br>details</span>
  </div>
  <div class="feature" style="left:277px; top:378px; font-size:25px; align-items:flex-start; gap:14px;">
    <svg width="46" height="52" viewBox="0 0 46 52"><rect x="12" y="4" width="28" height="40" rx="4"/><path d="M8 10 L6 44 a4 4 0 0 0 4 4 L30 48"/><circle cx="26" cy="24" r="7"/><path d="M21 24 H31"/></svg>
    <span>Silky smooth feel<br>that makes shuffling<br>easy</span>
  </div>
</section>

<!-- Square 4: Archival -->
<section class="module sq-archive">
  <div class="backdrop forest-fire-scene" role="img" aria-label="Burning fantasy forest with embers"></div>
  <div class="ribbon" style="left:17px; width:100px; height:178px; padding-top:40px;">
    <svg width="62" height="74" viewBox="0 0 62 74"><circle cx="31" cy="28" r="22"/><path d="M21 28 L28 35 L41 21"/><path d="M16 44 L8 66 L18 62 L22 72 L28 52"/><path d="M46 44 L54 66 L44 62 L40 72 L34 52"/></svg>
  </div>
  <h2 class="headline centered" style="top:126px; font-size:56px; line-height:1;">Archival-safe<br>high-quality<br>materials</h2>
  <p class="subline centered" style="top:292px; font-size:40px; line-height:1.05;">Acid-free, no PVC,<br>non-toxic, long-term<br>storage.</p>
  <div class="brand-ring" style="left:430px; top:450px; width:100px; height:100px;"></div>
</section>

<!-- Brand banner -->
<section class="module bn-brand">
  <div class="brand-ring" style="left:292px; top:64px; width:230px; height:230px;"></div>
  <div class="brand-name" style="left:572px; top:86px; font-size:100px;">Ember<br>Keep</div>
</section>

<!-- Banner: Shield -->
<section class="module bn-shield">
  <div class="backdrop fire-scene" role="img" aria-label="Dark background with glowing embers and flames"></div>
  <h2 class="headline" style="left:53px; top:56px; font-size:88px; line-height:.95;">Shield your cards<br>from wear</h2>
  <div class="feature" style="left:44px; top:242px; font-size:38px;">
    <svg width="66" height="64" viewBox="0 0 62 56"><path d="M6 10 L26 28 L6 46"/><path d="M18 6 L38 28 L18 50"/><path d="M40 28 H58 M52 22 L58 28 L52 34"/><circle cx="8" cy="28" r="1.5"/><circle cx="14" cy="20" r="1.5"/></svg>
    <span>Blocks<br>dust</span>
  </div>
  <div class="feature" style="left:280px; top:242px; font-size:38px;">
    <svg width="62" height="72" viewBox="0 0 62 72"><rect x="6" y="6" width="24" height="60" rx="3"/><path d="M36 14 L56 6 M34 36 L58 24 M36 58 L56 48"/></svg>
    <span>Resists surface<br>scratches.</span>
  </div>
  <div class="pack" style="left:903px; top:8px; width:282px; height:372px; transform:rotate(2deg);" role="img" aria-label="Ember Keep sleeves pack"></div>
  <div class="pack" style="left:763px; top:78px; width:206px; height:290px; transform:rotate(-2deg);" role="img" aria-label="Ember Keep sleeves pack"></div>
</section>

<!-- Banner: Fit -->
<section class="module bn-fit">
  <div class="backdrop fire-scene-top" role="img" aria-label="Dark background with flames along the edges"></div>
  <div class="pack" style="left:23px; top:100px; width:145px; height:280px;" role="img" aria-label="Ember Keep sleeves pack"></div>
  <div class="pack" style="left:146px; top:60px; width:274px; height:320px;" role="img" aria-label="Ember Keep sleeves pack"></div>
  <div class="pack" style="left:356px; top:120px; width:188px; height:250px;" role="img" aria-label="Ember Keep sleeves pack"></div>
  <h2 class="headline" style="left:606px; top:46px; font-size:82px; line-height:.95;">The perfect fit for<br>your collection</h2>
  <p class="subline" style="left:606px; top:212px; font-size:46px; line-height:1.05;">Designed to fit all standard<br>trading cards.</p>
</section>

<!-- Banner: Clear -->
<section class="module bn-clear">
  <div class="backdrop castle-scene" style="right:387px;" role="img" aria-label="Misty grey-blue fantasy castle backdrop"></div>
  <h2 class="headline" style="left:53px; top:50px; font-size:80px;">Ultra-clear smooth finish</h2>
  <div class="feature" style="left:72px; top:158px; font-size:29px;">
    <svg width="56" height="56" viewBox="0 0 46 46"><path d="M16 6 L19 17 L30 20 L19 23 L16 34 L13 23 L2 20 L13 17 Z"/><path d="M36 4 L37.5 9 L42 10.5 L37.5 12 L36 17 L34.5 12 L30 10.5 L34.5 9 Z"/><path d="M34 30 L35.5 35 L40 36.5 L35.5 38 L34 43 L32.5 38 L28 36.5 L32.5 35 Z"/></svg>
    <span>Enjoy crystal-clear visibility for vibrant artwork<br>and sharp details</span>
  </div>
  <div class="feature" style="left:72px; top:250px; font-size:29px;">
    <svg width="56" height="60" viewBox="0 0 46 52"><rect x="12" y="4" width="28" height="40" rx="4"/><path d="M8 10 L6 44 a4 4 0 0 0 4 4 L30 48"/><circle cx="26" cy="24" r="7"/><path d="M21 24 H31"/></svg>
    <span>Silky smooth feel that makes shuffling easy</span>
  </div>
  <div class="pack" style="left:829px; top:10px; width:366px; height:380px;" role="img" aria-label="Ember Keep protective card sleeves pack, 100 sleeves"></div>
</section>

<!-- Banner: Archival -->
<section class="module bn-archive">
  <div class="backdrop fire-scene" role="img" aria-label="Dark background framed by flames"></div>
  <div class="ribbon" style="left:76px; width:138px; height:242px; padding-top:80px;">
    <svg width="76" height="90" viewBox="0 0 62 74"><circle cx="31" cy="28" r="22"/><path d="M21 28 L28 35 L41 21"/><path d="M16 44 L8 66 L18 62 L22 72 L28 52"/><path d="M46 44 L54 66 L44 62 L40 72 L34 52"/></svg>
  </div>
  <h2 class="headline centered" style="top:56px; font-size:66px; line-height:.95;">Archival-safe<br>high-quality materials</h2>
  <p class="subline centered" style="top:190px; font-size:54px; line-height:1;">Acid-free, no PVC, non-toxic,<br>long-term storage.</p>
  <div class="brand-ring" style="left:975px; top:72px; width:190px; height:190px;"></div>
</section>

</body>
</html>
```